Modern Business Card

Modern professional business card with more than just logo and demographic info. Something memorable.

We are a trendy/modern chiropractic group with an emphasis on neurology, hence the minimalist-type brain logo. We want to convey that modern and technical aspect with professionalism and the elite nature of our practice environment.

```html
<!DOCTYPE html>
<html lang="en">
<head>
<meta charset="utf-8">
<title>Meridian Spine Studio – Business Card</title>
<link href="https://fonts.googleapis.com/css2?family=Montserrat:wght@300;400;500&family=Oswald:wght@600&display=swap" rel="stylesheet">
<style>
  :root {
    --bg: #e6e8eb;
    --card-white: #ffffff;
    --card-shade: #eef0f2;
    --brand-blue: #3b73b6;
    --brand-blue-deep: #2c5b95;
    --ink: #3a3d42;
    --logo-ink: #d9dde2;
  }
  * { margin: 0; padding: 0; box-sizing: border-box; }
  html, body {
    width: 1200px; height: 900px; overflow: hidden;
    background: var(--bg);
    font-family: "Montserrat", Arial, sans-serif;
  }
  .canvas {
    width: 1200px; height: 900px;
    display: flex; flex-direction: column; align-items: center; justify-content: center;
    gap: 40px;
  }
  .card {
    width: 700px; height: 400px; position: relative;
    box-shadow: 0 10px 30px rgba(0,0,0,0.18);
  }
  .card-front {
    background: radial-gradient(circle at 65% 55%, var(--card-white) 0%, var(--card-shade) 100%);
    color: var(--ink);
  }
  .identity {
    position: absolute; right: 385px; top: 128px; text-align: right;
  }
  .person-name {
    font-family: "Oswald", "Arial Narrow", sans-serif; font-weight: 600;
    font-size: 40px; letter-spacing: 0.5px; color: var(--brand-blue); line-height: 1;
    text-transform: uppercase;
  }
  .person-role {
    font-size: 17px; font-weight: 400; margin-top: 8px;
  }
  .divider {
    position: absolute; left: 345px; top: 135px; width: 2px; height: 110px;
    background: var(--brand-blue);
  }
  .contact-list {
    position: absolute; left: 380px; top: 145px; list-style: none;
  }
  .contact-item {
    display: flex; align-items: center; gap: 12px;
    font-size: 17px; line-height: 30px; font-weight: 400;
  }
  .contact-item svg { width: 15px; height: 15px; flex: none; }
  .web-highlight { color: var(--brand-blue); }
  .address {
    position: absolute; left: 70px; top: 300px; font-size: 17px; font-weight: 400;
  }
  .card-back {
    background: linear-gradient(135deg, var(--brand-blue) 0%, var(--brand-blue-deep) 100%);
    display: flex; align-items: center; justify-content: center;
  }
  .brand-lockup { display: flex; align-items: center; gap: 22px; }
  .brand-dot { width: 26px; height: 26px; background: var(--logo-ink); }
  .brand-name {
    font-weight: 300; color: var(--logo-ink); font-size: 46px; line-height: 1.1;
    letter-spacing: 3px; text-transform: uppercase;
  }
</style>
</head>
<body>
<main class="canvas">
  <section class="card card-front" aria-label="Card front">
    <div class="identity">
      <h1 class="person-name">Mark Ellison</h1>
      <p class="person-role">Director</p>
    </div>
    <div class="divider"></div>
    <ul class="contact-list">
      <li class="contact-item">
        <svg viewBox="0 0 16 16" aria-hidden="true"><path d="M4 1.5l2.2 3-1.3 1.6c.8 1.8 2.2 3.2 4 4l1.6-1.3 3 2.2-1.2 2.3C7.3 13 3 8.7 1.7 3.7z" fill="var(--brand-blue)"/></svg>
        (555) 310-2284
      </li>
      <li class="contact-item">
        <svg viewBox="0 0 16 16" aria-hidden="true"><rect x="1.5" y="3.5" width="13" height="9" fill="none" stroke="var(--brand-blue)" stroke-width="1.6"/><path d="M1.5 3.5L8 9l6.5-5.5" fill="none" stroke="var(--brand-blue)" stroke-width="1.6"/></svg>
        hello@meridianspine.com
      </li>
      <li class="contact-item">
        <svg viewBox="0 0 16 16" aria-hidden="true"><circle cx="8" cy="8" r="6.5" fill="var(--brand-blue)"/><path d="M1.5 8h13M8 1.5c-3 3.5-3 9.5 0 13M8 1.5c3 3.5 3 9.5 0 13" fill="none" stroke="#fff" stroke-width="1"/></svg>
        <span>www.<span class="web-highlight">meridianspine</span>.com</span>
      </li>
    </ul>
    <p class="address">1187 Cedar Ridge Lane Salem, OR 97301</p>
  </section>

  <section class="card card-back" aria-label="Card back">
    <div class="brand-lockup">
      <span class="brand-dot"></span>
      <p class="brand-name">Meridian<br>Spine Studio</p>
    </div>
  </section>
</main>
</body>
</html>
```